Oil and Gas Exploration and Production company needs a business card design

We need a business card design using our logo and colors in the logo. We want a mainstream design.

```html
<!DOCTYPE html>
<html lang="en">
<head>
<meta charset="utf-8">
<title>Aldera Oil &amp; Gas – Business Card</title>
<link rel="stylesheet" href="https://fonts.googleapis.com/css2?family=Work+Sans:wght@400;500;700&display=swap">
<style>
  :root {
    --backdrop: #2a2a2a;
    --card: #1c1c1c;
    --card-edge: #262626;
    --gold: #d9a52b;
    --white: #f4f4f4;
    --emboss: #3a3a3a;
    --emboss-light: #5c5c5c;
  }
  * { box-sizing: border-box; margin: 0; padding: 0; }
  html, body {
    width: 1200px; height: 900px; overflow: hidden;
    background: var(--backdrop);
    font-family: "Work Sans", sans-serif;
  }
  .canvas {
    width: 1200px; height: 900px;
    display: flex; flex-direction: column;
    align-items: center; justify-content: center; gap: 26px;
  }
  .card {
    width: 720px; height: 411px;
    background: linear-gradient(135deg, var(--card-edge), var(--card));
    position: relative;
  }

  /* Front */
  .card-front { display: flex; align-items: center; justify-content: center; }
  .front-brand { display: flex; align-items: center; gap: 18px; }
  .front-brand .brand-dot {
    width: 44px; height: 44px; border-radius: 50%;
    background: var(--emboss);
  }
  .front-brand .brand-name {
    font-weight: 700; font-size: 58px; line-height: 1.02;
    color: var(--emboss-light);
  }

  /* Back */
  .card-back {
    display: grid;
    grid-template-columns: 332px 2px 1fr;
    align-items: center;
  }
  .back-brand {
    display: flex; align-items: center; gap: 14px;
    justify-self: end; padding-right: 34px;
  }
  .back-brand .brand-dot {
    width: 36px; height: 36px; border-radius: 50%;
    background: var(--white);
  }
  .back-brand .brand-name {
    font-weight: 700; font-size: 40px; line-height: 1.02;
    color: var(--white);
  }
  .divider { width: 2px; height: 166px; background: var(--gold); }
  .contact { padding-left: 40px; color: var(--white); }
  .contact-name { color: var(--gold); font-weight: 500; font-size: 29px; line-height: 1.05; }
  .contact-role { font-size: 15px; margin-bottom: 18px; }
  .contact-address { font-size: 16px; line-height: 1.3; margin-bottom: 12px; }
  .contact-list { list-style: none; font-size: 16px; line-height: 1.45; }
  .contact-list li { display: flex; align-items: center; gap: 10px; }
  .contact-list svg { width: 12px; height: 12px; flex: none; }
  .web-accent { color: var(--gold); }
</style>
</head>
<body>
<main class="canvas">
  <section class="card card-front" aria-label="Card front">
    <div class="front-brand">
      <span class="brand-dot"></span>
      <span class="brand-name">Aldera<br>Oil &amp; Gas</span>
    </div>
  </section>

  <section class="card card-back" aria-label="Card back">
    <div class="back-brand">
      <span class="brand-dot"></span>
      <span class="brand-name">Aldera<br>Oil &amp; Gas</span>
    </div>
    <div class="divider"></div>
    <div class="contact">
      <p class="contact-name">Dale Whitford</p>
      <p class="contact-role">CFO</p>
      <p class="contact-address">2450 Cedar Ridge Rd,<br>Abilene, Texas us</p>
      <ul class="contact-list">
        <li>
          <svg viewBox="0 0 12 12" aria-hidden="true"><path d="M3 1 L5 3.5 L4 5 Q5 7 7 8 L8.5 7 L11 9 L10 11 Q4 11 1 4 Z" fill="none" stroke="#d9a52b" stroke-width="1.2" stroke-linejoin="round"/></svg>
          (555) 310-4826
        </li>
        <li>
          <svg viewBox="0 0 12 12" aria-hidden="true"><rect x="1" y="2.5" width="10" height="7" fill="none" stroke="#d9a52b" stroke-width="1.1"/><path d="M1 2.5 L6 6.5 L11 2.5" fill="none" stroke="#d9a52b" stroke-width="1.1"/></svg>
          info@alderaoilgas.com
        </li>
        <li>
          <svg viewBox="0 0 12 12" aria-hidden="true"><circle cx="6" cy="6" r="5" fill="none" stroke="#d9a52b" stroke-width="1.1"/><ellipse cx="6" cy="6" rx="2.2" ry="5" fill="none" stroke="#d9a52b" stroke-width="1"/><path d="M1 6 H11" stroke="#d9a52b" stroke-width="1"/></svg>
          <span>www.<span class="web-accent">alderaoilgas</span>.com</span>
        </li>
      </ul>
    </div>
  </section>
</main>
</body>
</html>
```